Amber Reed Properties, which offers a selection of prime properties (villas

A website that contains: Idea, benefits, destinations (villas), offers, about us, contact, newsletter, social media, blog, look at the attachment, even if it is in German. The idea is that I can easily add new pages, if necessary, with the design you make. Later on we want to add a reservation system, so you can book your villa through the internet. Besides, there is a concierge service available, which organizes everything for the customer, owner, from villa to restaurant, limo service, ... & benefits and emotions through nice pictures / videos, they should be convinced to invest.

Target Market(s)

Investors (golfer and non-golfer) which have 300'000 to invest in a kind of real-estate investing club

Number of Pages Required

5+ page

Font styles to use
Sans Serif

Requirements
Must have
• It must be for wordpress, must have an exclusive touch, high quality, with nice pictures of golf courses. The Logo is gold so it has to match with gold, the font is segan or segoe semilight or similar, sans serif
Nice to have
• may be as well as the possibility to include videos of the different destinations and houses

```html
<!DOCTYPE html>
<html lang="en">
<head>
<meta charset="utf-8">
<title>Amber Reed Properties</title>
<link rel="stylesheet" href="https://fonts.googleapis.com/css2?family=Open+Sans:wght@300;400;600&family=Great+Vibes&display=swap">
<style>
:root{
  --gold:#e2a92b;
  --gold-dark:#c8962a;
  --gold-soft:#d9ac4b;
  --ink:#333;
  --muted:#8a8a8a;
  --line:#e6e6e6;
  --footer:#c9ced6;
  --white:#fff;
}
*{margin:0;padding:0;box-sizing:border-box}
html,body{width:1200px;height:1200px;overflow:hidden;background:var(--white)}
body{font-family:"Open Sans",sans-serif;color:var(--ink);position:relative}
.page{position:absolute;left:412px;top:0;width:470px;height:1500px;transform:scale(.8);transform-origin:0 0;background:var(--white);box-shadow:0 0 6px rgba(0,0,0,.06)}
.abs{position:absolute}
.fill{position:absolute}
/* header */
.brand{left:58px;top:8px;width:72px;font-size:6px;color:var(--gold);font-weight:400;text-align:center;line-height:1}
.brand .mark{display:block;width:12px;height:12px;border:1px solid var(--gold);margin:0 auto 4px}
.nav-active{left:152px;top:0;width:30px;height:32px}
.nav{top:15px;font-size:4.5px;color:#555}
.nav-active span{position:absolute;top:15px;width:30px;text-align:center;font-size:4.5px;color:#fff}
.social{display:flex;gap:2px}
.social i{width:7px;height:7px;border:0.6px solid #777;border-radius:50%;display:block}
/* hero */
.hero{left:0;top:32px;width:470px;height:288px;background:linear-gradient(180deg,#e9d9a9 0%,#d9b57a 40%,#b99858 65%,#f4efe0 100%)}
.hero-box{left:114px;top:124px;width:270px;height:79px;background:rgba(120,120,120,.55)}
.hero-title{left:114px;top:146px;width:270px;text-align:center;color:#fff;font-weight:300;font-size:27px;letter-spacing:.3px}
.hero-btn{left:168px;top:194px;width:134px;height:17px;background:#fff;font-size:4.2px;text-align:center;line-height:17px;color:#333}
/* about */
.about{left:58px;top:266px;width:97px;height:319px;background:#fff;box-shadow:0 0 3px rgba(0,0,0,.12)}
.about-logo{left:4px;top:8px;width:89px;height:70px;border:1px solid var(--gold);display:flex;flex-direction:column;align-items:center;justify-content:flex-end;padding-bottom:4px;font-size:7.5px;color:var(--gold);font-weight:300}
.about-logo .mark{width:26px;height:26px;border:1px solid var(--gold);margin-bottom:8px}
.script{font-family:"Great Vibes",cursive;color:#444}
.about-script{left:4px;top:98px;font-size:30px}
.principle{left:0;top:145px;width:97px;height:29px;background:var(--gold);color:#fff;font-size:11px;padding:6px 4px}
.tiny{font-size:3.6px;line-height:5.8px;color:var(--muted)}
.principle-text{left:5px;top:183px;width:86px}
.readmore{font-size:3.6px;color:#555}
/* offer cards */
.card{top:266px;width:84px;height:164px;background:#fff;box-shadow:0 0 3px rgba(0,0,0,.1)}
.card .photo{left:0;top:0;width:84px;height:80px}
.card h3{position:absolute;left:3px;top:84px;font-size:8.5px;font-weight:400;color:#333}
.card .tiny{position:absolute;left:3px;top:97px;width:78px}
.card .bar{position:absolute;left:0;bottom:0;width:84px;height:14px;background:var(--gold);color:#fff;font-size:4px;line-height:14px;padding-left:4px}
/* video */
.video{left:157px;top:435px;width:254px;height:149px;background:linear-gradient(180deg,#6f7476 0%,#8b8f88 45%,#47533c 80%,#5d6b45 100%)}
.video-label{left:4px;top:6px;color:#fff;font-size:6px}
.video-all{right:22px;top:7px;color:var(--gold);font-size:4.5px}
.play{left:120px;top:68px;width:13px;height:13px}
/* newsletter */
.newsletter{left:58px;top:589px;width:353px;height:61px;background:linear-gradient(180deg,#d3a443,#c99730)}
.newsletter h2{position:absolute;top:6px;width:100%;text-align:center;color:#fff;font-size:10px;font-weight:400}
.nl-input{left:46px;top:35px;width:184px;height:14px;border-bottom:0.6px solid rgba(255,255,255,.6);color:#fff;font-size:4px;line-height:14px;padding-left:8px}
.nl-btn{left:231px;top:34px;width:80px;height:15px;background:#fff;font-size:4.5px;text-align:center;line-height:15px;color:#444}
/* section heads */
.section-script{width:470px;text-align:center;font-size:22px}
/* benefits */
.benefit-photo{position:absolute}
.benefit-title{font-size:17px;font-weight:300;color:var(--gold);line-height:16px}
.benefit-box{background:var(--gold);color:#fff;padding:15px 11px}
.benefit-box .lead{font-size:5px;font-weight:600;line-height:8px;margin-bottom:6px}
.benefit-box p{font-size:5px;font-weight:300;line-height:8px}
.know{position:absolute;width:75px;height:19px;background:var(--gold-dark);color:#fff;font-size:5px;text-align:center;line-height:19px}
/* blogs */
.blog{top:1175px;width:114px;height:160px;background:#fff;box-shadow:0 0 3px rgba(0,0,0,.1)}
.blog .photo{left:0;top:0;width:114px;height:102px}
.blog .tiny{position:absolute;left:4px;top:110px;width:104px}
.blog .readmore{position:absolute;left:4px;top:146px}
/* contact */
.contact-rule{left:58px;top:1360px;width:353px;height:1px;background:var(--line)}
.contact-title{left:58px;top:1365px;font-size:8px;color:#444}
.map{left:58px;top:1392px;width:127px;height:58px;background:linear-gradient(135deg,#e9eaec,#dcdfe3)}
.info{left:185px;top:1377px;width:226px;height:88px;border:1px solid var(--line);background:#fff}
.info-head{left:12px;top:13px;font-size:3.8px;color:#555}
.info-addr{left:12px;top:26px;font-size:3.8px;line-height:5.5px;color:#444}
.info-addr b{font-weight:600}
.info-contact{left:95px;top:29px;font-size:3.8px;line-height:9px;color:#444}
.info-contact div{display:flex;align-items:center;gap:6px}
.info-note{left:12px;top:64px;width:200px;font-size:3.4px;line-height:5px;color:#555}
.footer{left:0;top:1486px;width:470px;height:14px;background:var(--footer)}
.footer .copy{position:absolute;left:58px;top:4px;font-size:3.4px;color:#444}
.footer .social{position:absolute;left:364px;top:3px}
</style>
</head>
<body>
<div class="page">

  <!-- header -->
  <header>
    <div class="abs brand"><span class="mark"></span>AMBER REED PROPERTIES</div>
    <svg class="abs nav-active" viewBox="0 0 30 32"><path d="M0 0H30V27L15 32L0 27Z" fill="var(--gold)"/></svg>
    <div class="abs nav-active"><span>Idea</span></div>
    <div class="abs nav" style="left:184px">Benefits</div>
    <div class="abs nav" style="left:211px">Destinations</div>
    <div class="abs nav" style="left:248px">Offers</div>
    <div class="abs nav" style="left:272px">About us</div>
    <div class="abs nav" style="left:301px">Blog</div>
    <div class="abs nav" style="left:321px">Contact</div>
    <svg class="abs" style="left:343px;top:14px" width="7" height="7" viewBox="0 0 7 7"><circle cx="3" cy="3" r="2.2" fill="none" stroke="#333" stroke-width="1"/><path d="M4.6 4.6L6.6 6.6" stroke="#333" stroke-width="1"/></svg>
    <div class="abs social" style="left:364px;top:14px"><i></i><i></i><i></i><i></i><i></i></div>
  </header>

  <!-- hero -->
  <section class="fill hero" role="img" aria-label="Photo of a Mediterranean villa with palm trees and an infinity pool by the sea in golden light"></section>
  <div class="abs hero-box"></div>
  <h1 class="abs hero-title">Reach new heights</h1>
  <div class="abs hero-btn">INVEST ON US TO REACH THE POSSIBILITIES</div>

  <!-- about -->
  <aside class="abs about">
    <div class="abs about-logo"><span class="mark"></span>AMBER REED PROPERTIES</div>
    <div class="abs script about-script">About us</div>
    <div class="abs principle">Principle</div>
    <p class="abs tiny principle-text">As an investor, you become a member of the Amber Reed Owners Club, which regulates and organizes the use of the concierge service. Only 4 investors come to a property. This guarantees good availability with a planned use of 6 weeks each. An occupancy of 24 weeks is achieved. Up to 30 more weeks are rented to guests, and the rental income is shared among members each season. Your share can also be taken as credit for the next year.</p>
    <div class="abs readmore" style="left:5px;top:301px">READ MORE</div>
  </aside>

  <!-- destination cards -->
  <article class="abs card" style="left:157px">
    <div class="fill photo" role="img" aria-label="Photo of overwater bungalows in front of a green mountain island" style="background:linear-gradient(180deg,#6aa6d8 0%,#5f7d4a 50%,#2fb7c4 100%)"></div>
    <h3>Moutain Island</h3>
    <p class="tiny">A quiet villa above the lagoon with a private pool, sea views, and a golf course a short drive away. Concierge service arranges transfers, dining and tee times for each stay.</p>
    <div class="bar">Offer Details</div>
  </article>
  <article class="abs card" style="left:243px">
    <div class="fill photo" role="img" aria-label="Photo of an open terrace with a daybed overlooking green hills" style="background:linear-gradient(180deg,#b9c7cf 0%,#8f9a72 45%,#c9b48e 100%)"></div>
    <h3>Peace of City</h3>
    <p class="tiny">A quiet villa above the lagoon with a private pool, sea views, and a golf course a short drive away. Concierge service arranges transfers, dining and tee times for each stay.</p>
    <div class="bar">Offer Details</div>
  </article>
  <article class="abs card" style="left:328px">
    <div class="fill photo" role="img" aria-label="Photo of a colourful Mediterranean villa with palms and gardens" style="background:linear-gradient(180deg,#3f8fe0 0%,#c9a36a 50%,#3f7a3a 100%)"></div>
    <h3>Vintage talks</h3>
    <p class="tiny">A quiet villa above the lagoon with a private pool, sea views, and a golf course a short drive away. Concierge service arranges transfers, dining and tee times for each stay.</p>
    <div class="bar">Offer Details</div>
  </article>

  <!-- video -->
  <section class="abs video" role="img" aria-label="Video still of luxury cars parked on a lawn by a lake under a cloudy sky">
    <div class="abs video-label">See all videos</div>
    <div class="abs video-all">View all</div>
    <svg class="abs play" viewBox="0 0 13 13"><circle cx="6.5" cy="6.5" r="6" fill="rgba(0,0,0,.25)" stroke="#fff" stroke-width="0.8"/><path d="M5 4L9 6.5L5 9Z" fill="#fff"/></svg>
  </section>

  <!-- newsletter -->
  <section class="abs newsletter">
    <h2>Subscribe Our Newsletter</h2>
    <div class="abs nl-input">Email</div>
    <div class="abs nl-btn">SUBSCRIBE</div>
  </section>

  <!-- offers -->
  <div class="abs script section-script" style="left:0;top:668px">Offers</div>

  <div class="benefit-photo" role="img" aria-label="Photo of a thatched tropical resort with palm trees and a lagoon pool" style="left:58px;top:699px;width:190px;height:212px;background:linear-gradient(180deg,#4b8ed6 0%,#bcd3e6 35%,#3f6b34 60%,#8fa9a2 100%)"></div>
  <div class="abs benefit-title" style="left:258px;top:758px">Ihr Nutzen –<br>emotional</div>
  <div class="abs benefit-box" style="left:248px;top:789px;width:163px;height:122px">
    <div class="lead">Sie sind Mitbesitzer von exklusiven Immobilien in Topresorts, in wunderschöner, gepflegter und sicherer Umgebung</div>
    <p>Miteigentum ermöglicht Ihnen, Ihre Ferien an verschiedenen Destinationen zu verbringen – Abwechslung ist garantiert.<br>Sie geniessen.</p>
  </div>
  <div class="know" style="left:258px;top:884px">Know more</div>

  <div class="abs benefit-title" style="left:70px;top:966px">Ihr Nutzen -<br>praktisch</div>
  <div class="abs benefit-box" style="left:58px;top:1000px;width:164px;height:123px">
    <div class="lead">Sie sind Mitbesitzer von exklusiven Immobilien in Topresorts, in wunderschöner, gepflegter und sicherer Umgebung</div>
    <p>Miteigentum ermöglicht Ihnen, Ihre Ferien an verschiedenen Destinationen zu verbringen – Abwechslung ist garantiert.<br>Sie geniessen.</p>
  </div>
  <div class="know" style="left:70px;top:1095px">Know more</div>
  <div class="benefit-photo" role="img" aria-label="Photo of a stone villa at dusk with lit windows, lawn and stepping stone path" style="left:222px;top:911px;width:189px;height:212px;background:linear-gradient(180deg,#3d4f6e 0%,#a08a7a 40%,#1f2a22 60%,#3e6a36 100%)"></div>

  <!-- blogs -->
  <div class="abs script section-script" style="left:0;top:1140px">Blogs</div>
  <article class="abs blog" style="left:58px">
    <div class="fill photo" role="img" aria-label="Photo of a white stretch limousine in front of a grand building" style="background:linear-gradient(180deg,#8a7d63 0%,#5c5447 60%,#3b3e44 100%)"></div>
    <p class="tiny">As an investor you become a member of the owners club, which organizes the concierge service. Only four investors share a property, which guarantees good availability and an occupancy of 24 weeks.</p>
    <div class="readmore">READ MORE</div>
  </article>
  <article class="abs blog" style="left:178px">
    <div class="fill photo" role="img" aria-label="Photo of a beachfront hotel tower at sunset with palm trees" style="background:linear-gradient(180deg,#4a63a8 0%,#d894a8 55%,#e9c7a0 100%)"></div>
    <p class="tiny">As an investor you become a member of the owners club, which organizes the concierge service. Only four investors share a property, which guarantees good availability and an occupancy of 24 weeks.</p>
    <div class="readmore">READ MORE</div>
  </article>
  <article class="abs blog" style="left:297px">
    <div class="fill photo" role="img" aria-label="Photo of modern angular yellow and grey houses under a blue sky" style="background:linear-gradient(180deg,#5d95d8 0%,#c8b45a 55%,#6f7778 100%)"></div>
    <p class="tiny">As an investor you become a member of the owners club, which organizes the concierge service. Only four investors share a property, which guarantees good availability and an occupancy of 24 weeks.</p>
    <div class="readmore">READ MORE</div>
  </article>

  <!-- contact -->
  <div class="abs contact-rule"></div>
  <h2 class="abs contact-title" style="font-weight:400">Contact us</h2>
  <div class="abs map" role="img" aria-label="Street map showing the office location"></div>
  <svg class="abs" style="left:110px;top:1413px" width="5" height="7" viewBox="0 0 5 7"><path d="M2.5 7C2.5 7 0 4 0 2.5A2.5 2.5 0 0 1 5 2.5C5 4 2.5 7 2.5 7Z" fill="#d33"/></svg>
  <div class="abs info">
    <div class="abs info-head">INFORMATIONEN UND ANMELDUNG</div>
    <div class="abs info-addr"><b>Amber Reed Properties</b><br>c/o Fairway Advisory Group GmbH<br>Seeweg 12<br>CH-8000 Musterdorf<br>Zurich / Switzerland</div>
    <div class="abs info-contact">
      <div><svg width="5" height="5" viewBox="0 0 5 5"><path d="M1 0.5L2 1.8L1.5 2.4C2 3.2 2.3 3.5 2.9 3.8L3.5 3.2L4.6 4.2L4 4.8C2 4.6 0.3 2.8 0.3 1.1Z" fill="#333"/></svg>+41 00 000 00 00</div>
      <div style="margin-top:-5px;padding-left:11px">+41 00 000 00 01</div>
      <div><svg width="5" height="4" viewBox="0 0 5 4"><rect width="5" height="4" fill="#333"/><path d="M0 0L2.5 2L5 0" stroke="#fff" stroke-width="0.5" fill="none"/></svg>info@fairwayadvisory.example</div>
    </div>
    <p class="abs info-note">Please send us your questions or book a personal consultation. We look forward to hearing from you.<br><br>Your Amber Reed Properties Team</p>
  </div>

  <!-- footer -->
  <footer class="abs footer">
    <span class="copy">© Amber Reed Properties | 2016</span>
    <div class="social"><i></i><i></i><i></i><i></i><i></i></div>
  </footer>
</div>
</body>
</html>
```